A layout of a webpage for oil trade platform

I would like to have a desgin of one page webpage (with section scrollling dowin) that woulf present the new product i.e. oil trade platform for wholesale buyers and sellers.
Layout should consist of the sections similar to the given at: https://klinika.pewnywybor.pl/system-zarzadzania-wizytami
However oil industy require more colors and more photo stories than here for doctor.
I. I woul imagine at first below menu a slider with brueg information about the product and its advantages with "more" button next to the prict screen of our platform on different displays (PC and mobile).
II. Bellow the slider I would imagine icons correspoing to the advantages of that plaftorm:
1. Purchase/sale process automation 24/7
2. Access to the best deals
3. Electronic offerings and orderings
4. Transaction status monitoring
5. Data and transaction security
II A) (optional):
In near future we would like to prepare a short video presenation. Hence please prepare a place to display that element here.
At the moment alternatvily please prepare a How it works section that would explan the platform operating process
III. Next secion is about benefits for Oil Purchaser
It can be done either by icons of by text and corresponding grahip for while section.
Benefits:
- Access to cheaper oil
- Convenience of online orders
- Possibility to compare prices on the market
- Transaction history
- Order status monitoring
- Seccurity and transparency of purchase
IV. Next seciont is about benefits for Oil Seller
Benefits:
- New sale channel
- Attracting new clients
- More oil sold
- Transaction security
- Possibility to integrate with distribution infrastructure and logistits for more efficient automation.
V. Contact form
VI. Footer
I would need a layout that that will correspond to the very dynamic logo but I would expect also a clean form, smoth and modern. It has to be proffessional layout with more corporate character.
It can use a paralax features if needed.

```html
<!DOCTYPE html>
<html lang="en">
<head>
<meta charset="utf-8">
<title>Crudeway – Oil Trade Platform</title>
<link rel="stylesheet" href="https://fonts.googleapis.com/css2?family=Raleway:wght@300;400;500;600;700&display=swap">
<style>
:root{
  --orange:#f26a2b;
  --orange-soft:#f7a677;
  --navy:#16213c;
  --navy-deep:#0f1830;
  --ink:#2a2a2a;
  --grey:#7a7a7a;
  --field:#f0f0f0;
  --band:#ececec;
  --white:#ffffff;
  --black-bar:#1b1b1b;
}
*{margin:0;padding:0;box-sizing:border-box}
html,body{width:1200px;height:4033px;overflow:hidden}
body{position:relative;background:var(--white);font-family:'Raleway',sans-serif;color:var(--ink)}
.abs{position:absolute}
svg{display:block}

/* header */
.site-header{position:absolute;left:0;top:0;width:1200px;height:113px;background:var(--white);box-shadow:0 2px 6px rgba(0,0,0,.08);z-index:2}
.brand{position:absolute;display:flex;align-items:center;gap:14px}
.brand-dot{width:38px;height:38px;border-radius:50%;background:var(--orange)}
.brand-name{font-weight:700;font-size:30px;letter-spacing:1px;color:var(--navy)}
.main-nav{position:absolute;top:44px;left:343px;display:flex;gap:0}
.main-nav a{font-size:17px;letter-spacing:4px;color:var(--navy);text-decoration:none;font-weight:500;position:absolute;white-space:nowrap}
.main-nav a.active{font-weight:700}
.main-nav a.active::after{content:"";position:absolute;left:-20px;right:-16px;top:40px;height:3px;background:var(--navy)}

/* hero */
.hero{position:absolute;left:0;top:113px;width:1200px;height:572px}
.hero-photo{position:absolute;inset:0;background:linear-gradient(100deg,#8c8f93 0%,#b6b2ac 35%,#7b6f66 55%,#55504d 75%,#8a8d92 100%)}
.hero-card{position:absolute;left:166px;top:80px;width:250px;height:447px;background:rgba(40,40,45,.78)}
.hero-card .lead{height:130px;background:var(--orange);margin:0 12px;display:flex;align-items:center;justify-content:center;text-align:center;color:var(--white);font-weight:700;font-size:17px;letter-spacing:3px;line-height:33px}
.hero-card p{color:var(--white);text-align:center;font-size:19px;letter-spacing:4px;line-height:32px;padding:22px 20px;border-bottom:1px solid rgba(255,255,255,.5);margin:0 12px}
.hero-card p:last-child{border:none}
.hero-caption{position:absolute;left:618px;top:414px;width:500px;height:80px;background:linear-gradient(90deg,rgba(22,33,60,0) 0%,rgba(22,33,60,.92) 25%);display:flex;align-items:center;padding-left:80px;color:var(--white);font-weight:700;font-size:16px;letter-spacing:3px;line-height:28px}
.hero-caption .go{position:absolute;right:38px;top:18px;width:46px;height:46px;border:2px solid var(--white);border-radius:50%}
.hero-arrow{position:absolute;top:262px}

/* news band */
.news{position:absolute;left:0;top:685px;width:1200px;height:93px;background:var(--band)}
.news-text{position:absolute;left:255px;top:30px;font-size:15px;letter-spacing:2.5px;color:#555}
.news-date{position:absolute;left:255px;top:56px;font-size:10px;color:var(--orange);font-weight:600}

/* advantages */
.advantages{position:absolute;left:0;top:778px;width:1200px;height:704px}
.adv-visual{position:absolute;left:0;top:0;width:612px;height:704px;background:linear-gradient(160deg,#f4f6f6 0%,#dfe9e6 45%,#eef3f2 100%)}
.adv-divider{position:absolute;left:610px;top:0;width:5px;height:704px;background:var(--orange)}
.section-title{position:absolute;font-weight:400;letter-spacing:12px;white-space:nowrap;color:var(--ink)}
.section-title .accent{color:var(--orange)}
.bracket{position:absolute;border-bottom:2px solid var(--orange);border-right:2px solid var(--orange)}
.feature{position:absolute;text-align:center}
.feature-label{position:absolute;font-size:11px;color:var(--ink);white-space:nowrap}
.feature-label::before{content:"";display:inline-block;width:5px;height:5px;background:var(--ink);border-radius:50%;margin-right:6px;vertical-align:middle}
.ring{position:absolute;width:112px;height:112px;border-radius:50%;border:2px solid var(--orange-soft);display:flex;align-items:center;justify-content:center}
.ring .core{width:92px;height:92px;border-radius:50%;background:var(--white);border:2px solid var(--orange);display:flex;align-items:center;justify-content:center}
.ring.on .core{background:var(--orange)}
.deals-title{position:absolute;left:650px;width:520px;top:170px;text-align:center;font-size:38px;font-weight:300;letter-spacing:9px;color:var(--orange)}
.deals-copy{position:absolute;left:674px;width:468px;font-size:15px;line-height:24px;letter-spacing:3px;text-align:justify;color:#444}

/* purchaser */
.purchaser{position:absolute;left:0;top:1482px;width:1200px;height:916px}
.vertical-label{position:absolute;left:65px;top:730px;transform:rotate(-90deg);transform-origin:left top;font-size:56px;font-weight:300;letter-spacing:24px;color:#d4d4d4;white-space:nowrap}
.benefit{position:absolute;width:269px;height:129px;background:#f2f2f2;display:flex;align-items:center;gap:36px;padding-left:32px;font-size:15px;letter-spacing:2px;color:var(--orange)}
.benefit.highlight{background:var(--navy);border:3px solid #3c4b7a;align-items:flex-start;flex-direction:column;gap:10px;padding:20px 16px}
.benefit.highlight h3{font-size:15px;font-weight:700;color:var(--orange);letter-spacing:1px}
.benefit.highlight .row{display:flex;gap:14px;color:var(--white);font-size:14px;line-height:18px;letter-spacing:1px}
.hub{position:absolute;left:462px;top:362px;width:296px;height:296px;border-radius:50%;background:var(--orange-soft);padding:8px}
.hub-inner{width:100%;height:100%;border-radius:50%;background:#2d3447;border:4px solid var(--orange);display:flex;align-items:center;justify-content:center;text-align:center;color:var(--white);font-size:14px;line-height:19px;letter-spacing:1px;padding:0 70px}

/* seller */
.seller{position:absolute;left:0;top:2398px;width:1200px;height:770px;background:var(--navy)}
.seller-title{color:var(--white)}
.seller-sub{position:absolute;left:635px;top:175px;font-size:17px;font-style:italic;letter-spacing:4px;color:var(--white)}
.seller-head{position:absolute;left:62px;top:282px;font-size:34px;color:var(--white);font-weight:500;white-space:nowrap}
.seller-head::before{content:"";display:inline-block;width:11px;height:11px;border-radius:50%;background:var(--orange);margin-right:12px;vertical-align:middle}
.seller-copy{position:absolute;left:150px;width:400px;text-align:right;color:var(--white);font-size:15px;line-height:25px;letter-spacing:.5px}
.pager{position:absolute;top:618px;width:40px;height:40px;border:2px solid var(--orange);border-radius:50%}
.seller-frame{position:absolute;left:585px;top:268px;width:551px;height:422px;border:2px solid #6c7aa4;padding:12px}
.seller-photo{width:100%;height:100%;background:linear-gradient(115deg,#f4f4f2 0%,#d9d4cf 40%,#a99f98 70%,#efeae6 100%);position:relative}
.seller-strip{position:absolute;left:0;bottom:0;width:100%;height:128px;background:rgba(247,140,80,.82)}
.shop-pill{position:absolute;left:224px;top:95px;width:78px;height:20px;border-radius:10px;background:var(--navy);color:var(--white);font-size:10px;text-align:center;line-height:20px;letter-spacing:1px}

/* contact */
.contact{position:absolute;left:0;top:3168px;width:1200px;height:632px}
.contact-sub{position:absolute;left:0;width:1200px;top:140px;text-align:center;font-size:22px;letter-spacing:6px;color:#333}
.info-box{position:absolute;left:75px;width:75px;height:75px;border:1px solid #e6d6cc;display:flex;align-items:center;justify-content:center}
.info-text{position:absolute;left:163px;font-size:13px;line-height:17px;letter-spacing:1.5px;color:#333}
.field{position:absolute;background:var(--field);font-size:14px;color:#9a9a9a;padding:20px 18px;letter-spacing:1px}
.field.focus{background:var(--white);border:1px solid var(--orange-soft);box-shadow:0 4px 8px rgba(0,0,0,.15)}
.send{position:absolute;left:942px;top:553px;width:180px;height:41px;border:1px solid var(--orange-soft);color:var(--orange);font-size:13px;letter-spacing:1px;text-align:center;line-height:39px}

/* footer */
.site-footer{position:absolute;left:0;top:3800px;width:1200px;height:168px;background:var(--navy-deep)}
.site-footer .brand-name{color:var(--white);font-size:28px}
.tagline{position:absolute;left:140px;top:107px;font-size:11px;color:var(--white);letter-spacing:1px}
.updates-title{position:absolute;left:344px;top:56px;font-size:24px;letter-spacing:1px;color:var(--white)}
.updates-title span{color:var(--orange)}
.updates-note{position:absolute;left:344px;top:88px;font-size:12px;color:var(--white)}
.sub-input{position:absolute;left:690px;top:61px;width:188px;height:46px;background:var(--white)}
.sub-btn{position:absolute;left:878px;top:61px;width:183px;height:46px;background:var(--orange);color:var(--white);font-size:13px;letter-spacing:1px;text-align:center;line-height:46px}
.bottom-bar{position:absolute;left:0;top:3968px;width:1200px;height:65px;background:var(--black-bar)}
.copyright{position:absolute;left:349px;top:24px;font-size:13px;color:#ddd}
.copyright span{color:var(--orange)}
.social{position:absolute;top:22px;width:20px;height:20px;border-radius:50%;background:var(--white)}
</style>
</head>
<body>

<header class="site-header">
  <div class="brand" style="left:80px;top:34px"><span class="brand-dot"></span><span class="brand-name">Crudeway</span></div>
  <nav class="main-nav">
    <a class="active" href="#home" style="left:0">HOME</a>
    <a href="#advantages" style="left:106px">ADVANGE</a>
    <a href="#purchaser" style="left:253px">PURCHARSER</a>
    <a href="#seller" style="left:449px">SELLER</a>
    <a href="#contact" style="left:574px">CONTACT</a>
  </nav>
  <svg class="abs" style="left:1080px;top:44px" width="26" height="26" viewBox="0 0 26 26"><circle cx="11" cy="11" r="8" fill="none" stroke="var(--orange)" stroke-width="2.5"/><line x1="17" y1="17" x2="24" y2="24" stroke="var(--orange)" stroke-width="2.5"/></svg>
</header>

<section class="hero" id="home">
  <div class="hero-photo" role="img" aria-label="Photo of a woman refuelling her car at a petrol station"></div>
  <div class="hero-card">
    <div class="lead">THE BEST<br>DEAL ON THE<br>MARKET</div>
    <p>THE BEST<br>DEAL ON THE<br>MARKET</p>
    <p>THE BEST<br>DEAL ON THE<br>MARKET</p>
  </div>
  <svg class="hero-arrow" style="left:94px" width="24" height="40" viewBox="0 0 24 40"><polyline points="20,4 4,20 20,36" fill="none" stroke="#fff" stroke-width="3"/></svg>
  <svg class="hero-arrow" style="left:1082px" width="24" height="40" viewBox="0 0 24 40"><polyline points="4,4 20,20 4,36" fill="none" stroke="#fff" stroke-width="3"/></svg>
  <div class="hero-caption">LOREM IPSUM DOLOR<br>SIT AMET MASME TIN
    <svg class="go" viewBox="0 0 46 46"><polyline points="20,14 29,23 20,32" fill="none" stroke="#fff" stroke-width="2.5"/></svg>
  </div>
</section>

<div class="news">
  <svg class="abs" style="left:172px;top:22px" width="44" height="44" viewBox="0 0 44 44"><rect x="4" y="4" width="36" height="36" fill="none" stroke="var(--orange)" stroke-width="3"/><rect x="10" y="10" width="10" height="10" fill="var(--orange)"/><line x1="24" y1="12" x2="34" y2="12" stroke="var(--orange)" stroke-width="2"/><line x1="24" y1="18" x2="34" y2="18" stroke="var(--orange)" stroke-width="2"/><line x1="10" y1="26" x2="34" y2="26" stroke="var(--orange)" stroke-width="2"/><line x1="10" y1="32" x2="34" y2="32" stroke="var(--orange)" stroke-width="2"/></svg>
  <div class="news-text">VIVAMUS IMPERDIET, SUSPENDISSE IMPERDIET NULLA INTEGER LITORA PURUS</div>
  <div class="news-date">23 MAY 17</div>
  <svg class="abs" style="left:1030px;top:32px" width="36" height="28" viewBox="0 0 36 28"><path d="M4 10h6l14-8v24L10 18H4z" fill="none" stroke="var(--orange)" stroke-width="2.5"/><path d="M29 8q4 6 0 12M32 5q6 9 0 18" fill="none" stroke="var(--orange)" stroke-width="2"/></svg>
</div>

<section class="advantages" id="advantages">
  <div class="adv-visual" role="img" aria-label="Faded photo of a fuel pump nozzle"></div>
  <div class="adv-divider"></div>
  <h2 class="section-title" style="left:75px;top:86px;font-size:46px">THE <span class="accent">ADVANGE</span></h2>
  <div class="bracket" style="left:220px;top:78px;width:310px;height:72px"></div>

  <div class="feature-label" style="left:75px;top:240px">Purchase Sale</div>
  <div class="feature-label" style="left:285px;top:240px">the best deals</div>
  <div class="feature-label" style="left:470px;top:240px">Orders</div>
  <div class="feature-label" style="left:165px;top:453px">Status Order</div>
  <div class="feature-label" style="left:372px;top:453px">Security Pay</div>

  <div class="ring" style="left:75px;top:266px"><div class="core">
    <svg width="48" height="36" viewBox="0 0 48 36"><rect x="2" y="6" width="40" height="26" fill="none" stroke="#333" stroke-width="2.5"/><rect x="6" y="2" width="40" height="26" fill="#fff" stroke="#333" stroke-width="2.5"/><circle cx="26" cy="15" r="6" fill="none" stroke="#333" stroke-width="2.5"/></svg></div></div>
  <div class="ring on" style="left:272px;top:266px"><div class="core">
    <svg width="44" height="40" viewBox="0 0 44 40"><path d="M2 4h7l6 22h22l5-16H12" fill="none" stroke="#fff" stroke-width="3"/><circle cx="17" cy="34" r="3" fill="#fff"/><circle cx="34" cy="34" r="3" fill="#fff"/></svg></div></div>
  <div class="ring" style="left:467px;top:266px"><div class="core">
    <svg width="48" height="40" viewBox="0 0 48 40"><path d="M12 30H10a8 8 0 0 1 0-16 12 12 0 0 1 23-2 9 9 0 0 1 5 18h-2" fill="none" stroke="#333" stroke-width="2.5"/><path d="M24 38V18M17 25l7-7 7 7" fill="none" stroke="#333" stroke-width="2.5"/></svg></div></div>
  <div class="ring" style="left:170px;top:482px"><div class="core">
    <svg width="40" height="40" viewBox="0 0 40 40"><rect x="3" y="7" width="28" height="30" fill="none" stroke="#333" stroke-width="2.5"/><path d="M14 26l2-7 16-16 5 5-16 16z" fill="#fff" stroke="#333" stroke-width="2.5"/></svg></div></div>
  <div class="ring" style="left:374px;top:482px"><div class="core">
    <svg width="36" height="42" viewBox="0 0 36 42"><path d="M9 18v-6a9 9 0 0 1 18 0v6" fill="none" stroke="#333" stroke-width="2.5"/><rect x="4" y="18" width="28" height="22" fill="none" stroke="#333" stroke-width="2.5"/></svg></div></div>

  <h2 class="deals-title">THE BEST DEALS</h2>
  <p class="deals-copy" style="top:292px">Lorem ipsum dolor sit amet, consectetur adipisicing elit, sed do eiusmod tempor incididunt ut labore et dolore magna aliqua. Ut enim ad minim.</p>
  <p class="deals-copy" style="top:432px">mmodo consequat. Duis aute irure dolor in reprehenderit in voluptate velit esse cillum dolore eu fugiat nulla pariatur. Excepteur sint occaecat cupidatat non proident, sunt in culpa qui officia deserunt mollit anim</p>
  <svg class="abs" style="left:848px;top:630px" width="30" height="30" viewBox="0 0 30 30"><circle cx="23" cy="6" r="3.5" fill="none" stroke="#333" stroke-width="2"/><circle cx="7" cy="15" r="3.5" fill="none" stroke="#333" stroke-width="2"/><circle cx="23" cy="24" r="3.5" fill="none" stroke="#333" stroke-width="2"/><path d="M10 13l10-5M10 17l10 5" stroke="#333" stroke-width="2"/></svg>
  <svg class="abs" style="left:930px;top:628px" width="34" height="32" viewBox="0 0 34 32"><path d="M3 13L17 3l14 10v16H3z" fill="none" stroke="#333" stroke-width="2"/><path d="M3 13l14 10 14-10M3 29l11-9M31 29l-11-9" fill="none" stroke="#333" stroke-width="2"/></svg>
</section>

<section class="purchaser" id="purchaser">
  <h2 class="section-title" style="left:578px;top:128px;font-size:44px"><span class="accent">OIL</span> PURCHARSER</h2>
  <div class="bracket" style="left:712px;top:118px;width:422px;height:72px"></div>
  <div class="vertical-label">THE BENEFITS</div>

  <div class="benefit highlight" style="left:166px;top:274px;width:269px;height:129px">
    <h3>Acces to Cheaper</h3>
    <div class="row">
      <svg width="50" height="34" viewBox="0 0 50 34"><rect x="2" y="2" width="46" height="30" rx="3" fill="none" stroke="#fff" stroke-width="2.5"/><line x1="2" y1="11" x2="48" y2="11" stroke="#fff" stroke-width="4"/><line x1="8" y1="23" x2="22" y2="23" stroke="#fff" stroke-width="2"/></svg>
      <span>Sed at facilisis<br>lacus, non mattis<br>augue.</span>
    </div>
  </div>
  <div class="benefit" style="left:166px;top:481px">
    <svg width="34" height="44" viewBox="0 0 34 44"><path d="M17 2q10 10 8 28H9Q7 12 17 2z" fill="none" stroke="#333" stroke-width="2.5"/><circle cx="17" cy="16" r="3.5" fill="none" stroke="#333" stroke-width="2"/><path d="M9 24l-6 8 6 0M25 24l6 8-6 0M14 34v8M20 34v8" fill="none" stroke="#333" stroke-width="2"/></svg>
    <span>Online Orders</span></div>
  <div class="benefit" style="left:166px;top:688px">
    <svg width="40" height="40" viewBox="0 0 40 40"><path d="M33 14A14 14 0 0 0 8 11M7 26a14 14 0 0 0 25 3" fill="none" stroke="#333" stroke-width="2.5"/><path d="M34 6v9h-9M6 34v-9h9" fill="none" stroke="#333" stroke-width="2.5"/></svg>
    <span>Compare Prices</span></div>
  <div class="benefit" style="left:797px;top:274px">
    <svg width="36" height="40" viewBox="0 0 36 40"><ellipse cx="18" cy="7" rx="15" ry="5" fill="none" stroke="#333" stroke-width="2.5"/><path d="M3 7v26c0 6 30 6 30 0V7M3 16c0 6 30 6 30 0M3 25c0 6 30 6 30 0" fill="none" stroke="#333" stroke-width="2.5"/></svg>
    <span>History Sells</span></div>
  <div class="benefit" style="left:797px;top:481px">
    <svg width="36" height="40" viewBox="0 0 36 40"><path d="M4 10h28v28H4z" fill="none" stroke="#333" stroke-width="2.5"/><path d="M12 10v4a6 6 0 0 0 12 0v-4" fill="none" stroke="#333" stroke-width="2.5"/></svg>
    <span>Order Status</span></div>
  <div class="benefit" style="left:797px;top:688px">
    <svg width="36" height="42" viewBox="0 0 36 42"><path d="M18 2l14 6v12c0 10-7 17-14 20C11 37 4 30 4 20V8z" fill="none" stroke="#333" stroke-width="2.5"/><path d="M12 15l12 12M24 15L12 27" stroke="#333" stroke-width="2.5"/></svg>
    <span>Purcharse Secure</span></div>

  <div class="hub"><div class="hub-inner">Sed at facilisis lacus, non mattis augue. Nulla nec semper massa. Aliquam erat volutpat. Morbi id posuere massa.</div></div>
</section>

<section class="seller" id="seller">
  <svg class="abs" style="left:0;top:0" width="1200" height="60" viewBox="0 0 1200 60"><polygon points="0,0 1200,0 1200,0 1200,20 600,0 0,20" fill="#fff"/><polygon points="0,0 1200,0 1200,30 600,0 0,30" fill="#fff"/></svg>
  <h2 class="section-title seller-title" style="left:425px;top:108px;font-size:44px">OIL <span class="accent">SELLER</span></h2>
  <div class="bracket" style="left:555px;top:100px;width:240px;height:62px;border-color:#fff"></div>
  <div class="seller-sub">THE BENEFITS</div>
  <div class="seller-head">ATTRACTING NEW CLIENTES</div>
  <p class="seller-copy" style="top:360px">BIBENDUM RIDICULUS ENIM AENEAN SUSCIPIT, MASSA FERMENTUM GRAVIDA ELIT DONEC, QUIS URNA ETIAM, UT AC SED SED UT MOLLIS, QUIS NEQUE PER LIBERO CRAS VESTIBULUM EST</p>
  <p class="seller-copy" style="top:490px">LUCTUS JUSTO ELIT LOBORTIS, LACUS FERMENTUM, VIVAMUS BLANDIT SCELERISQUE IPSUM.</p>
  <svg class="pager" style="left:232px" viewBox="0 0 40 40"><polyline points="23,12 15,20 23,28" fill="none" stroke="var(--orange)" stroke-width="2.5"/></svg>
  <svg class="pager" style="left:328px" viewBox="0 0 40 40"><polyline points="17,12 25,20 17,28" fill="none" stroke="var(--orange)" stroke-width="2.5"/></svg>
  <div class="seller-frame">
    <div class="seller-photo" role="img" aria-label="Photo of a smiling couple looking at a laptop together">
      <div class="seller-strip">
        <svg class="abs" style="left:110px;top:32px" width="40" height="40" viewBox="0 0 40 40"><circle cx="20" cy="20" r="17" fill="none" stroke="#333" stroke-width="2.5"/><line x1="20" y1="17" x2="20" y2="30" stroke="#333" stroke-width="3"/><circle cx="20" cy="11" r="2" fill="#333"/></svg>
        <svg class="abs" style="left:245px;top:28px" width="36" height="40" viewBox="0 0 36 40"><rect x="3" y="14" width="30" height="24" fill="none" stroke="#333" stroke-width="2.5"/><rect x="1" y="9" width="34" height="6" fill="none" stroke="#333" stroke-width="2.5"/><line x1="18" y1="9" x2="18" y2="38" stroke="#333" stroke-width="2.5"/><path d="M18 9q-10-10-10-2M18 9q10-10 10-2" fill="none" stroke="#333" stroke-width="2"/></svg>
        <div class="shop-pill">SHOP</div>
        <svg class="abs" style="left:378px;top:32px" width="44" height="40" viewBox="0 0 44 40"><path d="M3 4h24v16H13l-6 6v-6H3z" fill="none" stroke="#333" stroke-width="2.5"/><path d="M31 12h10v16h-4v6l-6-6H17v-4" fill="none" stroke="#333" stroke-width="2.5"/></svg>
      </div>
    </div>
  </div>
</section>

<section class="contact" id="contact">
  <h2 class="section-title" style="left:345px;top:60px;font-size:46px"><span class="accent">CONTACT</span> FORM</h2>
  <div class="bracket" style="left:338px;top:56px;width:512px;height:66px;border-right:2px solid var(--orange);border-left:2px solid var(--orange)"></div>
  <div class="contact-sub">ANY SUGGESTIONS</div>

  <div class="info-box" style="top:212px"><svg width="26" height="34" viewBox="0 0 26 34"><path d="M13 32S3 19 3 12a10 10 0 0 1 20 0c0 7-10 20-10 20z" fill="none" stroke="var(--orange)" stroke-width="2.5"/><circle cx="13" cy="12" r="4" fill="none" stroke="var(--orange)" stroke-width="2.5"/></svg></div>
  <div class="info-text" style="top:222px">48 Harbour Lane<br>E14 2QT<br>London</div>
  <div class="info-box" style="top:365px"><svg width="22" height="34" viewBox="0 0 22 34"><rect x="2" y="2" width="18" height="30" rx="2" fill="none" stroke="var(--orange)" stroke-width="2.5"/><line x1="8" y1="27" x2="14" y2="27" stroke="var(--orange)" stroke-width="2"/></svg></div>
  <div class="info-text" style="top:338px">+44 (20) 555 0141<br>+44 (20) 555 0172<br>+44 (20) 555 0198</div>
  <div class="info-box" style="top:497px"><svg width="32" height="24" viewBox="0 0 32 24"><rect x="2" y="2" width="28" height="20" fill="none" stroke="var(--orange)" stroke-width="2.5"/><path d="M2 2l14 11L30 2" fill="none" stroke="var(--orange)" stroke-width="2.5"/></svg></div>
  <div class="info-text" style="top:468px">info@crudeway.example<br>sales@crudeway.example</div>

  <div class="field" style="left:523px;top:215px;width:269px;height:59px">Name</div>
  <div class="field" style="left:854px;top:215px;width:268px;height:59px">Email</div>
  <div class="field focus" style="left:523px;top:296px;width:599px;height:59px">Subject</div>
  <div class="field" style="left:523px;top:376px;width:599px;height:156px">Comments</div>
  <div class="send">SEND MESSAGE</div>
</section>

<footer class="site-footer">
  <div class="brand" style="left:80px;top:48px"><span class="brand-dot"></span><span class="brand-name">Crudeway</span></div>
  <div class="tagline">Wholesale and retail</div>
  <div class="updates-title">GET <span>UPDATES</span></div>
  <div class="updates-note">subscribe to our newsletter and get latest news from us</div>
  <div class="sub-input"></div>
  <div class="sub-btn">SUBSCRIBE NOW</div>
</footer>
<div class="bottom-bar">
  <div class="copyright"><span>© 2017 Crudeway.</span> All Rights Reserved.</div>
  <span class="social" style="left:997px"></span>
  <span class="social" style="left:1042px"></span>
  <span class="social" style="left:1090px"></span>
</div>

</body>
</html>
```